Business Cards Brookvale
Biz_cards_Brookvale
Professional
Dwight Omsen, MD, PhD
418 Pennock Hollow Rd
Jackson, TN 38305
domsen@brookvalespine.com
www.brookvalespine.com
Here is logo specs:
Brookvale Spine Institute
Fonts:
Trajan Pro (Regular)
" " " " (Bold)
Colors:
Dark Blue : R: 3 G: 34 B: 87
Light Blue : R: 0 G: 102 B: 187
Dark Red : R: 130 G: 0 B: 0
Light Green : R: 255 G: 0 B: 0

```html
<!DOCTYPE html>
<html lang="en">
<head>
<meta charset="utf-8">
<title>Brookvale Spine Institute – Stationery</title>
<link href="https://fonts.googleapis.com/css2?family=Cinzel:wght@400;700&family=Open+Sans:wght@400;600&display=swap" rel="stylesheet">
<style>
:root{
  --dark-blue:#032257;
  --light-blue:#0066bb;
  --dark-red:#820000;
  --red:#ff0000;
  --paper:#ffffff;
  --stage:#a4a5a7;
  --ink:#3a3a3a;
  --muted:#8a8a8a;
}
*{box-sizing:border-box;margin:0;padding:0}
html,body{width:1200px;height:247px;overflow:hidden;background:var(--stage)}
body{position:relative;font-family:"Open Sans",Arial,sans-serif;color:var(--ink)}
.item{position:absolute;box-shadow:0 1px 3px rgba(0,0,0,.35)}
.paper{background:var(--paper)}
.navy{background:radial-gradient(circle at 40% 40%,var(--light-blue),var(--dark-blue) 75%)}
.label{position:absolute;font-size:6px;color:#eee;letter-spacing:.2px}

.brand{display:flex;align-items:center;gap:3px;font-family:"Cinzel",serif;font-weight:700;color:var(--dark-blue);line-height:1}
.brand-dot{border-radius:50%;background:var(--dark-red);flex:none}
.brand-name{text-transform:uppercase}
.brand.on-dark{color:#fff}

.presenter-brand{position:absolute;left:30px;top:12px}
.presenter-brand .brand-dot{width:14px;height:14px}
.presenter-brand .brand-name{font-size:9px}

/* business cards */
.card-front .brand{position:absolute;left:50%;top:50%;transform:translate(-50%,-50%)}
.card-front .brand-dot{width:8px;height:8px}
.card-front .brand-name{font-size:6px}
.card-info{position:absolute;right:5px;bottom:5px;font-size:3.4px;line-height:1.35;text-align:right;color:var(--ink)}
.card-info b{display:block;font-family:"Cinzel",serif;color:var(--dark-blue);font-size:4.4px}
.card-stripe{position:absolute;left:0;right:0;bottom:0;height:4px;background:var(--dark-blue);border-top:1px solid var(--red)}
.card-logo{position:absolute;left:5px;top:5px}
.card-logo .brand-dot{width:6px;height:6px}
.card-logo .brand-name{font-size:4.5px}

/* letterhead */
.letterhead{width:112px;height:204px;top:26px}
.letterhead .card-logo{left:8px;top:9px}
.letterhead .card-logo .brand-dot{width:9px;height:9px}
.letterhead .card-logo .brand-name{font-size:5.5px}
.letter-body{position:absolute;left:10px;right:12px;top:44px;font-size:3.3px;line-height:1.6;color:var(--muted)}
.letter-body p{margin-bottom:4px}
.sign-line{width:30px;height:1px;background:var(--dark-blue);margin:10px 0 2px}
.letter-foot{position:absolute;left:0;right:0;bottom:0;height:13px;background:linear-gradient(90deg,var(--dark-blue),var(--light-blue));border-top:1.5px solid var(--red);color:#fff;font-size:3px;display:flex;align-items:center;justify-content:center}

/* envelopes */
.envelope-flap{position:absolute;inset:0}
.envelope .card-logo{top:6px}

/* folder */
.folder{left:930px;top:18px;width:260px;height:212px;display:flex}
.folder-panel{flex:1;position:relative;background:radial-gradient(circle at 50% 45%,#1a5fae,var(--dark-blue) 70%)}
.folder-panel + .folder-panel{border-left:1px solid rgba(255,255,255,.2)}
.folder-cover .brand{position:absolute;left:50%;top:58%;transform:translateX(-50%);flex-direction:column;gap:4px;text-align:center}
.folder-cover .brand-dot{width:16px;height:16px}
.folder-cover .brand-name{font-size:8px}
.folder-pocket{position:absolute;left:0;right:0;bottom:0;height:70px}
.folder-wave{position:absolute;right:0;top:0;height:100%;width:40px}
</style>
</head>
<body>

<div class="presenter-brand brand on-dark"><span class="brand-dot"></span><span class="brand-name">Brookvale<br>Spine Institute</span></div>

<!-- business card set -->
<div class="item navy card-front" style="left:12px;top:62px;width:86px;height:48px">
  <div class="brand on-dark"><span class="brand-dot"></span><span class="brand-name">Brookvale</span></div>
</div>
<span class="label" style="left:104px;top:82px">Business Cards</span>

<div class="item navy card-front" style="left:12px;top:120px;width:86px;height:46px">
  <div class="brand on-dark"><span class="brand-dot"></span><span class="brand-name">Brookvale</span></div>
</div>
<div class="item paper" style="left:106px;top:120px;width:86px;height:46px">
  <div class="card-logo brand"><span class="brand-dot"></span><span class="brand-name">Brookvale</span></div>
  <div class="card-info"><b>Dwight Omsen, MD, PhD</b>418 Pennock Hollow Rd<br>Jackson, TN 38305<br>domsen@brookvalespine.com</div>
  <div class="card-stripe"></div>
</div>

<div class="item paper card-front" style="left:12px;top:178px;width:86px;height:46px">
  <div class="brand"><span class="brand-dot"></span><span class="brand-name">Brookvale</span></div>
</div>
<div class="item paper" style="left:106px;top:178px;width:86px;height:46px">
  <div class="card-logo brand"><span class="brand-dot"></span><span class="brand-name">Brookvale</span></div>
  <div class="card-info"><b>Dwight Omsen, MD, PhD</b>www.brookvalespine.com<br>Jackson, TN 38305</div>
  <div class="card-stripe"></div>
</div>

<!-- letterheads -->
<div class="item paper letterhead" style="left:268px">
  <div class="card-logo brand"><span class="brand-dot"></span><span class="brand-name">Brookvale<br>Spine Institute</span></div>
  <div class="letter-body">
    <p>Dear Patient,</p>
    <p>Thank you for choosing our clinic for your care. We look forward to seeing you soon.</p>
    <p>Sincerely,</p>
    <div class="sign-line"></div>Dwight Omsen, MD, PhD
  </div>
  <div class="letter-foot">418 Pennock Hollow Rd · Jackson, TN 38305 · www.brookvalespine.com</div>
</div>
<div class="item paper letterhead" style="left:392px">
  <div class="card-logo brand"><span class="brand-dot"></span><span class="brand-name">Brookvale<br>Spine Institute</span></div>
  <div class="letter-body">
    <p>Dear Patient,</p>
    <p>Thank you for choosing our clinic for your care. We look forward to seeing you soon.</p>
    <p>Sincerely,</p>
    <div class="sign-line"></div>Dwight Omsen, MD, PhD
  </div>
  <div class="letter-foot">418 Pennock Hollow Rd · Jackson, TN 38305 · www.brookvalespine.com</div>
</div>
<span class="label" style="left:430px;top:234px">Letterhead</span>

<!-- cards and slips -->
<div class="item paper card-front" style="left:530px;top:28px;width:100px;height:56px">
  <div class="brand"><span class="brand-dot"></span><span class="brand-name">Brookvale</span></div>
  <div class="card-stripe"></div>
</div>
<div class="item paper" style="left:642px;top:28px;width:100px;height:56px">
  <div class="card-logo brand"><span class="brand-dot"></span><span class="brand-name">Brookvale</span></div>
  <div class="card-info"><b>Dwight Omsen, MD, PhD</b>418 Pennock Hollow Rd<br>Jackson, TN 38305<br>domsen@brookvalespine.com<br>www.brookvalespine.com</div>
  <div class="card-stripe"></div>
</div>
<div class="item navy card-front" style="left:530px;top:118px;width:100px;height:44px">
  <div class="brand on-dark"><span class="brand-dot"></span><span class="brand-name">Brookvale</span></div>
</div>
<div class="item paper" style="left:530px;top:172px;width:200px;height:54px">
  <div class="card-logo brand"><span class="brand-dot"></span><span class="brand-name">Brookvale Spine Institute</span></div>
  <div class="card-info">418 Pennock Hollow Rd · Jackson, TN 38305<br>www.brookvalespine.com</div>
  <div class="card-stripe"></div>
</div>

<!-- envelopes -->
<div class="item navy envelope" style="left:760px;top:100px;width:140px;height:62px">
  <svg class="envelope-flap" viewBox="0 0 140 62" preserveAspectRatio="none"><path d="M0 0 L70 34 L140 0" fill="none" stroke="rgba(255,255,255,.35)" stroke-width="1"/><rect y="56" width="140" height="6" fill="#ff0000" opacity=".8"/></svg>
</div>
<div class="item paper envelope" style="left:760px;top:170px;width:140px;height:56px">
  <div class="card-logo brand"><span class="brand-dot"></span><span class="brand-name">Brookvale</span></div>
  <div class="card-stripe"></div>
</div>
<span class="label" style="left:760px;top:234px">Envelope</span>

<!-- presentation folder -->
<div class="item folder">
  <div class="folder-panel folder-cover">
    <div class="brand on-dark"><span class="brand-dot"></span><span class="brand-name">Brookvale<br>Spine Institute</span></div>
  </div>
  <div class="folder-panel">
    <svg class="folder-wave" viewBox="0 0 40 212" preserveAspectRatio="none">
      <path d="M40 0 L22 0 C6 40 30 80 14 120 C2 160 26 190 18 212 L40 212 Z" fill="#fff"/>
      <path d="M40 0 L28 0 C12 40 36 80 20 120 C8 160 32 190 24 212 L40 212 Z" fill="#820000"/>
      <path d="M40 0 L34 0 C20 40 42 80 28 120 C16 160 38 190 32 212 L40 212 Z" fill="#ff0000"/>
    </svg>
    <svg class="folder-pocket" viewBox="0 0 130 70" preserveAspectRatio="none"><path d="M0 12 Q65 0 130 12 L130 70 L0 70 Z" fill="rgba(3,34,87,.6)" stroke="rgba(255,255,255,.3)" stroke-width=".6"/></svg>
  </div>
</div>
<span class="label" style="left:1160px;top:234px">Folder</span>

</body>
</html>
```